Professional business card design for Shelfwright Company
Biz card design utilizing existing Logo
Professional business card design for Shelfwright Company - Construction
Creative Brief
Use same font as used in my logo
Dean Halvik
President
not necessary
dean@brvmarrow.com
www.brvmarrow.com

```html
<!DOCTYPE html>
<html lang="en">
<head>
<meta charset="utf-8">
<title>Shelfwright Company – Business Card</title>
<link rel="stylesheet" href="https://fonts.googleapis.com/css2?family=Oswald:wght@300;400;600&display=swap">
<style>
  :root {
    --backdrop: #dcdcdc;
    --card: #ffffff;
    --green: #4e9a2f;
    --ink: #2b2b2b;
    --ink-soft: #555555;
  }
  * { margin: 0; padding: 0; box-sizing: border-box; }
  html, body { width: 1200px; height: 947px; overflow: hidden; }
  body {
    background: var(--backdrop);
    font-family: "Oswald", "Arial Narrow", sans-serif;
    color: var(--ink);
    position: relative;
  }
  .card {
    position: absolute;
    left: 250px;
    width: 700px;
    height: 400px;
    background: var(--card);
    border-radius: 22px;
    box-shadow: 0 6px 18px rgba(0,0,0,0.12);
  }
  .card--back { top: 50px; }
  .card--front { top: 497px; }

  /* back */
  .back-brand {
    position: absolute;
    left: 0; right: 0; top: 150px;
    display: flex; align-items: center; justify-content: center; gap: 16px;
  }
  .brand-square { width: 54px; height: 54px; background: var(--green); flex: none; }
  .back-brand .brand-name {
    font-weight: 600; font-size: 40px; letter-spacing: 1px;
    color: var(--green); text-transform: uppercase;
  }
  .social {
    position: absolute; right: 34px; bottom: 28px;
    display: flex; gap: 22px;
  }
  .social-item {
    display: flex; align-items: center; gap: 7px;
    font-size: 13px; font-weight: 300; color: var(--ink-soft);
  }
  .social-item .dot { width: 16px; height: 16px; background: var(--ink); }

  /* front */
  .front-brand {
    position: absolute; left: 44px; top: 150px;
    display: flex; align-items: center; gap: 14px;
  }
  .front-brand .brand-square { width: 64px; height: 64px; }
  .front-brand .brand-name {
    font-weight: 600; font-size: 34px; line-height: 1.0;
    color: var(--green); text-transform: uppercase;
  }
  .contact { position: absolute; left: 380px; top: 52px; }
  .person {
    display: flex; align-items: stretch; gap: 14px; margin-bottom: 34px;
  }
  .bar { width: 4px; background: var(--ink); flex: none; }
  .person-name {
    font-weight: 600; font-size: 30px; letter-spacing: 1px;
    text-transform: uppercase; line-height: 1.1;
  }
  .person-title { font-weight: 300; font-size: 14px; color: var(--ink-soft); }
  .row {
    display: flex; align-items: center; gap: 14px; margin-bottom: 24px;
  }
  .row .icon { width: 34px; height: 34px; flex: none; }
  .row .bar { align-self: stretch; width: 3px; }
  .row-text { font-weight: 300; font-size: 15px; line-height: 1.35; color: var(--ink-soft); }
</style>
</head>
<body>

<section class="card card--back">
  <div class="back-brand">
    <span class="brand-square"></span>
    <span class="brand-name">Shelfwright Company</span>
  </div>
  <div class="social">
    <span class="social-item"><span class="dot"></span>/brvmarrow</span>
    <span class="social-item"><span class="dot"></span>@brvmarrow</span>
  </div>
</section>

<section class="card card--front">
  <div class="front-brand">
    <span class="brand-square"></span>
    <span class="brand-name">Shelfwright<br>Company</span>
  </div>

  <div class="contact">
    <div class="person">
      <span class="bar"></span>
      <div>
        <div class="person-name">Dean Halvik</div>
        <div class="person-title">President</div>
      </div>
    </div>

    <div class="row">
      <svg class="icon" viewBox="0 0 34 34" aria-hidden="true">
        <circle cx="17" cy="11" r="7" fill="var(--green)"/>
        <path d="M4 32c0-8 6-12 13-12s13 4 13 12z" fill="var(--green)"/>
      </svg>
      <span class="bar"></span>
      <div class="row-text">Mobile<br>014 550 2761</div>
    </div>

    <div class="row">
      <svg class="icon" viewBox="0 0 34 34" aria-hidden="true">
        <path d="M17 2c-6.6 0-11 4.8-11 10.6C6 20 17 32 17 32s11-12 11-19.4C28 6.8 23.6 2 17 2z" fill="var(--green)"/>
        <circle cx="17" cy="12.5" r="4" fill="#fff"/>
      </svg>
      <span class="bar"></span>
      <div class="row-text">27 Alder Row<br>Kestrel Park</div>
    </div>

    <div class="row">
      <svg class="icon" viewBox="0 0 34 34" aria-hidden="true">
        <circle cx="17" cy="17" r="15" fill="var(--green)"/>
        <g fill="none" stroke="#fff" stroke-width="1.6">
          <ellipse cx="17" cy="17" rx="6.5" ry="15"/>
          <line x1="2" y1="17" x2="32" y2="17"/>
          <path d="M5 9.5h24M5 24.5h24"/>
        </g>
      </svg>
      <span class="bar"></span>
      <div class="row-text">dean@brvmarrow.com<br>www.brvmarrow.com</div>
    </div>
  </div>
</section>

</body>
</html>
```